Waistline Crest Product Social Media Graphics

Focusing on the Waistline Crest product, create 5-6 individual social media graphics (square size). For the color scheme of the graphics, they should all be complementary with the Waistline Crest bottle colors.
Note: each graphic should have one of the 2 pictures of the bottle on it and/or one of the images with a person on it (several pics attached)/only use stock photography that I provided.
Target Market(s)
For men and women trying to lose belly fat
Industry/Entity Type
health and wellness
Look and feel
Each slider illustrates characteristics of the customer's brand and the style your logo design should communicate.

```html
<!DOCTYPE html>
<html lang="en">
<head>
<meta charset="utf-8">
<title>Waistline Crest Social Graphics</title>
<link rel="stylesheet" href="https://fonts.googleapis.com/css2?family=Lato:wght@400;700;900&display=swap">
<style>
:root{
  --red:#e8402e;
  --red-deep:#d8332a;
  --coral:#f06a55;
  --pink:#f7b3ae;
  --ink:#262626;
  --text:#3a3a3a;
  --white:#ffffff;
  --photo-grey:#dcd9d7;
  --skin:#b9785a;
  --page:#ffffff;
}
*{margin:0;padding:0;box-sizing:border-box}
html,body{width:1200px;height:823px;overflow:hidden;background:var(--page)}
body{position:relative;font-family:'Lato',sans-serif}
.tile{position:absolute;width:348px;height:348px;background:var(--white);overflow:hidden;box-shadow:0 0 3px rgba(0,0,0,.12)}
.tile svg.bg{position:absolute;left:0;top:0}
.abs{position:absolute}
.photo-block{position:absolute}
.bottles{position:absolute;border-radius:6px;background:linear-gradient(180deg,#fbfbfb 0%,#eeeeee 55%,#e8402e 56%,#e8402e 70%,#f4f4f4 71%)}
.headline{position:absolute;font-weight:900;text-transform:uppercase;line-height:1.18;letter-spacing:-.2px}
.headline .hot{color:var(--red)}
.headline .dark{color:var(--ink)}
.benefits{position:absolute;list-style:none}
.benefits li{display:flex;align-items:center;font-size:8.5px;color:var(--text)}
.benefits .icon{width:28px;height:28px;border-radius:50%;background:var(--red);margin-right:8px;display:flex;align-items:center;justify-content:center;flex:none}
</style>
</head>
<body>

<!-- Tile 1 -->
<section class="tile" style="left:40px;top:47px">
  <svg class="bg" width="348" height="348" viewBox="0 0 348 348">
    <path d="M0 0H348V30Q340 170 210 190Q110 205 40 150Q5 115 0 60Z" fill="var(--red)"/>
    <path d="M0 0H340V20Q330 160 205 182Q108 196 40 142Q8 110 0 60Z" fill="#d0c7c2"/>
    <rect x="0" y="325" width="348" height="23" fill="var(--coral)"/>
  </svg>
  <div class="photo-block" role="img" aria-label="Close-up of a woman's midriff with hands forming a heart over the belly" style="left:30px;top:0;width:280px;height:150px;background:radial-gradient(ellipse at 55% 45%,#c48463 0%,#a8694b 55%,rgba(208,199,194,0) 80%)"></div>
  <div class="bottles" role="img" aria-label="Three Waistline Crest supplement bottles" style="left:265px;top:120px;width:78px;height:68px"></div>
  <div class="bottles" role="img" aria-label="Three Waistline Crest supplement bottles" style="left:4px;top:285px;width:60px;height:52px"></div>
  <h2 class="headline" style="left:0;width:348px;top:210px;text-align:center;font-size:24px;line-height:1.2">
    <span class="hot">Belly Bloat No More</span><br>
    <span class="dark">Discover the secret to<br>a flatter tummy!</span>
  </h2>
</section>

<!-- Tile 2 -->
<section class="tile" style="left:427px;top:47px">
  <svg class="bg" width="348" height="348" viewBox="0 0 348 348">
    <path d="M196 0H348V50H262Q205 48 196 0Z" fill="var(--pink)"/>
    <path d="M205 0H348V40H268Q215 38 205 0Z" fill="var(--red)"/>
    <path d="M0 45Q188 40 188 200V348H0Z" fill="var(--photo-grey)"/>
  </svg>
  <div class="photo-block" role="img" aria-label="Fit woman in white sports bra and briefs showing toned waist" style="left:20px;top:55px;width:140px;height:293px;background:linear-gradient(180deg,#efeeee 0%,#c58a6b 30%,#b6775a 60%,#ececec 75%,#b6775a 100%);border-radius:60px 60px 0 0"></div>
  <div class="bottles" role="img" aria-label="Three Waistline Crest supplement bottles" style="left:245px;top:10px;width:72px;height:62px"></div>
  <h2 class="headline" style="right:12px;top:83px;text-align:right;font-size:19px;line-height:1.38">
    <span class="hot">Reduce belly fat</span><br>
    <span class="dark">and bloating<br>overnight!</span>
  </h2>
  <ul class="benefits" style="left:224px;top:176px">
    <li style="height:39px"><span class="icon"><svg width="14" height="14" viewBox="0 0 14 14"><rect x="3" y="2" width="8" height="10" rx="2" fill="#fff"/></svg></span>Flatter tummy</li>
    <li style="height:38px"><span class="icon"><svg width="14" height="14" viewBox="0 0 14 14"><circle cx="7" cy="7" r="5" fill="none" stroke="#fff" stroke-width="1.6"/></svg></span>Reduced bloating</li>
    <li style="height:38px"><span class="icon"><svg width="14" height="14" viewBox="0 0 14 14"><rect x="2" y="3" width="10" height="8" rx="3" fill="#fff"/></svg></span>Improved digestion</li>
    <li style="height:38px"><span class="icon"><svg width="14" height="14" viewBox="0 0 14 14"><path d="M8 1L3 8H7L6 13L11 6H7Z" fill="#fff"/></svg></span>Increased energy</li>
  </ul>
</section>

<!-- Tile 3 -->
<section class="tile" style="left:814px;top:47px">
  <svg class="bg" width="348" height="348" viewBox="0 0 348 348">
    <path d="M0 0H45Q50 80 0 105Z" fill="var(--pink)"/>
    <path d="M0 0H50Q55 55 0 80Z" fill="var(--red)"/>
    <path d="M325 0H348V20Q330 20 325 0Z" fill="var(--red)"/>
    <path d="M168 348V96Q230 70 348 78V348Z" fill="#e9e7e6"/>
    <path d="M210 90Q270 72 330 78" fill="none" stroke="var(--red)" stroke-width="2.5"/>
    <rect x="160" y="175" width="5" height="173" fill="var(--red)"/>
  </svg>
  <div class="photo-block" role="img" aria-label="Smiling woman in a red sports top holding out oversized jeans" style="left:168px;top:96px;width:180px;height:252px;background:linear-gradient(180deg,#e9e7e6 0%,#6b4a3a 20%,#a6664a 35%,#e0485a 45%,#e0485a 62%,#a6664a 70%,#6f8fb3 88%,#6f8fb3 100%)"></div>
  <div class="bottles" role="img" aria-label="Three Waistline Crest supplement bottles" style="left:123px;top:88px;width:98px;height:88px"></div>
  <h2 class="headline" style="left:69px;top:15px;font-size:20px;line-height:1.35">
    <span class="dark">Get rid of toxins to</span><br>
    <span class="hot">reveal a flatter tummy!</span>
  </h2>
  <ul class="benefits" style="left:11px;top:112px">
    <li style="height:52px"><span class="icon"><svg width="14" height="14" viewBox="0 0 14 14"><rect x="3" y="2" width="8" height="10" rx="2" fill="#fff"/></svg></span>Flatter tummy</li>
    <li style="height:50px"><span class="icon"><svg width="14" height="14" viewBox="0 0 14 14"><circle cx="7" cy="7" r="5" fill="none" stroke="#fff" stroke-width="1.6"/></svg></span>Reduced bloating</li>
    <li style="height:50px"><span class="icon"><svg width="14" height="14" viewBox="0 0 14 14"><rect x="2" y="3" width="10" height="8" rx="3" fill="#fff"/></svg></span>Improved digestion</li>
    <li style="height:52px"><span class="icon"><svg width="14" height="14" viewBox="0 0 14 14"><path d="M8 1L3 8H7L6 13L11 6H7Z" fill="#fff"/></svg></span>Increased energy</li>
  </ul>
</section>

<!-- Tile 4 -->
<section class="tile" style="left:40px;top:429px">
  <svg class="bg" width="348" height="348" viewBox="0 0 348 348">
    <rect x="0" y="0" width="348" height="196" fill="var(--red)"/>
    <rect x="15" y="15" width="320" height="200" rx="18" fill="var(--white)"/>
  </svg>
  <div class="photo-block" role="img" aria-label="Slim woman in white crop top holding out loose jeans beside product bottles" style="left:17px;top:17px;width:316px;height:196px;border-radius:16px;background:linear-gradient(90deg,#9c5f43 0%,#b7795b 18%,#6f8fb3 30%,#d9d9da 45%,#e3e3e4 100%)"></div>
  <div class="bottles" role="img" aria-label="Three Waistline Crest supplement bottles" style="left:173px;top:44px;width:146px;height:128px"></div>
  <h2 class="headline" style="left:0;width:348px;top:238px;text-align:center;font-size:23px;line-height:1.18">
    <span class="hot">Belly Bloat No More</span><br>
    <span class="dark">Discover the secret to<br>a flatter tummy!</span>
  </h2>
</section>

<!-- Tile 5 -->
<section class="tile" style="left:427px;top:429px">
  <svg class="bg" width="348" height="348" viewBox="0 0 348 348">
    <path d="M0 0H48V40Q48 45 43 45H0Z" fill="var(--pink)"/>
    <path d="M0 0H42V34Q42 38 38 38H0Z" fill="var(--red)"/>
    <path d="M250 5Q300 20 334 60V300Q300 335 250 343Q200 335 168 300V60Q200 20 250 5Z" fill="var(--red-deep)"/>
    <path d="M250 43Q296 55 326 90V240Q296 278 250 290Q204 278 174 240V90Q204 55 250 43Z" fill="var(--white)"/>
  </svg>
  <div class="photo-block" role="img" aria-label="Woman's midriff with hands forming a heart over the belly" style="left:179px;top:52px;width:142px;height:230px;clip-path:polygon(50% 0,100% 18%,100% 78%,50% 100%,0 78%,0 18%);background:radial-gradient(ellipse at 50% 50%,#b8795b 0%,#a8694b 55%,#c9c3c0 80%)"></div>
  <div class="bottles" role="img" aria-label="Three Waistline Crest supplement bottles" style="left:190px;top:215px;width:120px;height:108px"></div>
  <h2 class="headline" style="left:23px;top:66px;font-size:24px;line-height:1.34">
    <span class="hot">Want a<br>flatter<br>stomach?<br>This gut</span><br>
    <span class="dark">cleanse<br>could be<br>the key!</span>
  </h2>
</section>

<!-- Tile 6: product shot -->
<div class="bottles" role="img" aria-label="Three Waistline Crest supplement bottles, product shot" style="left:853px;top:465px;width:270px;height:238px;border-radius:14px"></div>

</body>
</html>
```